Life and business Coaching Business Card and Logo

A new design for new company. We coach people to get the best out of themselves in business, life, health , family, career, relationships.
we work in Professional, executive, business and corporate environment. We use art and the processes of making art to work with getting people to delve into and change their mind maps or the way they are currently thinking so that they can move forward towards their goals strategically.
Updates

Project Deadline Extended
Reason: I have been laid up in bed with back problems and have just been able to get back to view designs. several are quiet good and I have given feedback today. I also want to take my project off refundable status as I will choose a design from this brief. regards Marisol

Target Market(s)

Professional artistic and bold energetic individuals

Industry/Entity Type

Health

Contact Information for Business Card

Velmora Mentoring, Marisol Drayke, Shaping Days Boldly,
Mob:0419586740, Ph: +61 8 95820647,
Professional, Executive, Business and Corporate Coach

Requirements
Must have
• a logo that can be used on all promotional and stationary material.
Should contain a person and be bold/colourful, simple and artistic.
Nice to have
• Room to place qualifications of Business

```html
<!DOCTYPE html>
<html lang="en">
<head>
<meta charset="utf-8">
<title>Velmora Mentoring – Marisol Drayke</title>
<link rel="stylesheet" href="https://fonts.googleapis.com/css2?family=Cinzel:wght@400;700&family=Great+Vibes&family=Pinyon+Script&family=Tinos&display=swap">
<style>
  :root {
    --ink: #000000;
    --gold: #f7ec1e;
    --silver: #d4d4d4;
    --steel-light: #e8e8e8;
    --steel-mid: #8d8f92;
    --steel-dark: #3b3d40;
    --cyan: #23e6f2;
    --tag-cyan: #36d8e8;
    --tag-green: #3cd04a;
    --tag-yellow: #f5e51c;
    --tag-orange: #f39a1e;
    --tag-red: #e5231e;
  }
  * { margin: 0; padding: 0; box-sizing: border-box; }
  html, body { width: 1200px; height: 741px; overflow: hidden; background: var(--ink); }
  .card {
    position: relative;
    width: 1200px;
    height: 741px;
    background: var(--ink);
    overflow: hidden;
    font-family: "Cinzel", serif;
  }
  .portrait {
    position: absolute;
    left: 32px;
    top: 38px;
    width: 492px;
    height: 703px;
  }
  .brand {
    position: absolute;
    right: 11px;
    top: 58px;
    font-family: "Tinos", serif;
    font-weight: 400;
    font-size: 72px;
    line-height: 1;
    color: var(--gold);
    white-space: nowrap;
  }
  .name {
    position: absolute;
    right: 11px;
    top: 180px;
    font-family: "Great Vibes", cursive;
    font-size: 86px;
    line-height: 1.1;
    color: var(--gold);
    letter-spacing: 4px;
    white-space: nowrap;
  }
  .role {
    position: absolute;
    right: 11px;
    top: 302px;
    text-align: right;
    font-family: "Cinzel", serif;
    font-size: 28px;
    line-height: 38px;
    color: var(--silver);
    white-space: nowrap;
  }
  .contact {
    position: absolute;
    right: 11px;
    top: 420px;
    text-align: right;
    color: var(--silver);
    font-family: "Cinzel", serif;
    font-weight: 700;
    font-variant-numeric: lining-nums;
  }
  .contact p { line-height: 60px; white-space: nowrap; }
  .contact .label { font-size: 32px; }
  .contact .number { font-size: 58px; letter-spacing: 1px; }
  .links {
    position: absolute;
    right: 11px;
    top: 546px;
    text-align: right;
    font-family: "Tinos", serif;
    font-size: 24px;
    line-height: 36px;
    color: var(--cyan);
    white-space: nowrap;
  }
  .tagline {
    position: absolute;
    left: 420px;
    top: 612px;
    font-family: "Pinyon Script", cursive;
    font-size: 78px;
    line-height: 1.2;
    white-space: nowrap;
    background: linear-gradient(90deg, var(--tag-cyan) 0%, var(--tag-green) 28%, var(--tag-yellow) 52%, var(--tag-orange) 74%, var(--tag-red) 100%);
    -webkit-background-clip: text;
    background-clip: text;
    color: transparent;
  }
</style>
</head>
<body>
<main class="card">
  <svg class="portrait" viewBox="0 0 492 703" role="img" aria-label="Illustration of a metallic head in profile with a multicoloured brain">
    <defs>
      <linearGradient id="steel" x1="0" y1="0" x2="1" y2="1">
        <stop offset="0" stop-color="var(--steel-mid)"/>
        <stop offset="0.45" stop-color="var(--steel-light)"/>
        <stop offset="0.75" stop-color="var(--steel-mid)"/>
        <stop offset="1" stop-color="var(--steel-dark)"/>
      </linearGradient>
    </defs>
    <rect x="0" y="0" width="492" height="703" rx="200" ry="200" fill="url(#steel)"/>
  </svg>

  <h1 class="brand">Velmora Mentoring</h1>
  <p class="name">Marisol Drayke</p>
  <p class="role">Professional, Executive,<br>Business and Corporate Coach</p>

  <div class="contact">
    <p><span class="label">Mob:</span><span class="number">0419586740</span></p>
    <p><span class="label">ph:</span><span class="number">+61 8 95820647</span></p>
  </div>

  <div class="links">
    <p>web: www.velmoramentoring.com</p>
    <p>email: marisol.drayke@kestrelnet.com</p>
  </div>

  <p class="tagline">Shaping Days Boldly</p>
</main>
</body>
</html>
```